Unternehmen für Wimpernverlängerung & -lifting benötigt Flyer-Design
Zielgruppe
Wimpernverlängerung, Wimpernlifting, Permanent Make-Up, Microblading, BB Glow, Hyaluron Pen
Aufgabenstellung
es soll eine preisliste werden, ich möchte die preise selbst einsetzen
produkte:
Wimpernverlängerung:
Natural Look
Auffüllen bis 1-2 Wochen
Auffüllen bis 3-4 Wochen
Ab der 5. Woche Neupreis
Volumen Look
Wimpernlifting inkl. färben
Microblading
Permanent Make-Up:
Powder Brows
Powder Brows Combo (Härchen&Shading)
Wimpernkranzverdichtung
Lidstrich dekorativ
Aquarelle Lips
Lippen Vollschattierung
BB Glow
Hyaluron Pen
Termine nach Vereinbarung

```html
<!DOCTYPE html>
<html lang="de">
<head>
<meta charset="utf-8">
<title>Lumi Lash – Flyer &amp; Preisliste</title>
<link rel="stylesheet" href="https://fonts.googleapis.com/css2?family=Fira+Sans:ital,wght@0,300;0,400;0,600;1,300&family=Fira+Sans+Condensed:wght@300&family=Josefin+Sans:wght@400;600&display=swap">
<style>
  :root {
    --stage: #2e1331;
    --paper: #fbfafb;
    --plum-dark: #4e0f50;
    --plum-mid: #6b3a6e;
    --rose: #d3749c;
    --rose-light: #e9a9c2;
    --rose-soft: #f0b8cb;
    --white: #ffffff;
    --skin-light: #e7c2ad;
    --skin-dark: #b98a73;
    --body: "Fira Sans", sans-serif;
    --cond: "Fira Sans Condensed", sans-serif;
    --head: "Josefin Sans", sans-serif;
  }
  * { box-sizing: border-box; margin: 0; padding: 0; }
  html, body { width: 1200px; height: 800px; overflow: hidden; }
  body { background: var(--stage); position: relative; font-family: var(--body); }

  .flyer {
    position: absolute; top: 35px;
    width: 360px; height: 730px;
    background: var(--paper);
    overflow: hidden;
  }
  .flyer--intro { left: 225px; }
  .flyer--prices { left: 620px; }
  .flyer__art { position: absolute; inset: 0; width: 360px; height: 730px; }

  /* Intro flyer */
  .intro__headline {
    position: absolute; left: 44px; top: 176px;
    font-family: var(--cond); font-weight: 300;
    font-size: 13px; line-height: 16px; letter-spacing: 0.5px;
    color: var(--plum-dark);
  }
  .services { position: absolute; left: 44px; top: 226px; width: 296px; list-style: none; }
  .service { margin-bottom: 11px; }
  .service__name {
    font-family: var(--head); font-weight: 600;
    font-size: 10px; letter-spacing: 1.4px; color: var(--plum-dark);
    line-height: 14px;
  }
  .service__text { font-size: 7px; line-height: 12px; color: var(--rose); font-weight: 300; }
  .service__text--narrow { width: 205px; }
  .intro__portrait {
    position: absolute; left: 267px; top: 238px;
    width: 78px; height: 78px; border-radius: 50%;
    background: radial-gradient(circle at 45% 40%, var(--skin-light), var(--skin-dark) 70%, #5a3a35);
    border: 2px solid var(--plum-dark);
  }
  .brand-name { font-family: var(--body); font-weight: 300; letter-spacing: 0.5px; }
  .intro__brand { position: absolute; left: 44px; top: 594px; font-size: 22px; color: var(--white); }
  .intro__contact { position: absolute; left: 36px; top: 643px; font-size: 10px; line-height: 15px; color: var(--white); }
  .intro__phone {
    position: absolute; right: 37px; top: 640px; text-align: right;
    font-size: 16px; font-weight: 600; color: var(--white);
  }
  .tag {
    display: inline-block; font-size: 6.5px; font-weight: 600; letter-spacing: 0.3px;
    padding: 2px 7px; color: var(--white);
  }
  .tag--rose { background: var(--rose-light); }
  .tag--plum { background: var(--plum-dark); }
  .intro__phone .tag { margin-top: 4px; width: 111px; text-align: center; }
  .intro__rule { position: absolute; left: 36px; right: 37px; top: 690px; border-top: 1px solid var(--rose-soft); }
  .intro__social {
    position: absolute; left: 36px; right: 37px; top: 703px;
    display: flex; justify-content: space-between; align-items: center;
    font-size: 9px; color: var(--white); list-style: none;
  }
  .intro__social li { display: flex; align-items: center; gap: 4px; }
  .dot { width: 11px; height: 11px; border-radius: 50%; background: var(--rose-light); display: inline-block; }

  /* Price flyer */
  .prices__title {
    position: absolute; left: 27px; top: 22px;
    font-family: var(--cond); font-weight: 300; font-size: 13px; letter-spacing: 1px;
    color: var(--plum-dark);
  }
  .price-list { position: absolute; left: 27px; right: 29px; top: 160px; }
  .price-group { margin-bottom: 12px; }
  .price-group__title {
    font-family: var(--head); font-weight: 600; font-size: 11.5px; letter-spacing: 1.6px;
    color: var(--plum-dark); line-height: 18px;
  }
  .price-group__sub { font-size: 10px; font-weight: 600; color: var(--rose); line-height: 15px; }
  .price-row { display: flex; font-size: 10px; font-weight: 300; color: var(--rose); line-height: 15px; letter-spacing: 0.3px; }
  .price-row__label { flex: 1; }
  .price-row__unit { width: 20px; }
  .price-row__cur { width: 14px; }
  .price-row__amt { width: 30px; text-align: right; }
  .price-note { font-size: 7.5px; font-style: italic; font-weight: 300; color: var(--rose); line-height: 14px; margin-bottom: 14px; }
  .gap-sm { margin-top: 4px; }
  .prices__footer { position: absolute; left: 27px; top: 686px; }
  .prices__web { font-size: 10px; font-weight: 600; color: var(--rose); margin-top: 6px; }
  .prices__brand { position: absolute; right: 24px; top: 693px; font-size: 19px; color: var(--plum-dark); }
</style>
</head>
<body>

<article class="flyer flyer--intro">
  <svg class="flyer__art" viewBox="0 0 360 730" aria-hidden="true">
    <defs>
      <linearGradient id="introPhoto" x1="0" y1="0" x2="0" y2="1">
        <stop offset="0" stop-color="#e9cbb9"/>
        <stop offset="1" stop-color="#c99c86"/>
      </linearGradient>
    </defs>
    <rect width="360" height="112" fill="url(#introPhoto)" role="img" aria-label="Foto: geschlossene Augen mit langen Wimpern"/>
    <path d="M0,76 C90,100 210,116 360,92 L360,110 C250,132 120,130 0,102 Z" fill="var(--plum-dark)"/>
    <path d="M0,102 C120,130 250,132 360,110 L360,160 L0,160 Z" fill="var(--paper)"/>
    <path d="M0,467 C120,475 240,520 360,560 L360,730 L0,730 Z" fill="var(--plum-dark)"/>
    <path d="M0,508 C140,516 250,562 360,606 L360,730 L0,730 Z" fill="var(--plum-mid)"/>
  </svg>

  <h2 class="intro__headline">LASHES, BROWN, PERMANENT MAKE-UP<br>IN BIRKENRIED UND UMGEBUNG</h2>

  <ul class="services">
    <li class="service">
      <h3 class="service__name">WIMPERNVERLÄNGERUNG</h3>
      <p class="service__text service__text--narrow">Schöne, dichte Wimpern. Mit einem sehr guten Tragekomfort ohne Schädigung der Naturwimpern.</p>
    </li>
    <li class="service">
      <h3 class="service__name">WIMPERNLIFTING</h3>
      <p class="service__text service__text--narrow">Schön geschwungene Wimpern, die natürlich wirken, da mit den eigenen Wimpern gearbeitet wird.</p>
    </li>
    <li class="service">
      <h3 class="service__name">PERMANENT MAKE-UP</h3>
    </li>
    <li class="service">
      <h3 class="service__name">MICROBLADING</h3>
      <p class="service__text">Schonende und dauerhaften Pigmentierung von Augenbrauen-Härchen.</p>
    </li>
    <li class="service">
      <h3 class="service__name">BB GLOW</h3>
      <p class="service__text">Für ein dauerhaft ausgeglichenes Hautbild mit natürlichem Glow.</p>
    </li>
    <li class="service">
      <h3 class="service__name">HYALURON PEN</h3>
    </li>
  </ul>

  <div class="intro__portrait" role="img" aria-label="Foto: Wimpernverlängerung mit Pinzette"></div>

  <p class="intro__brand brand-name">LUMI LASH</p>

  <p class="intro__contact">Mirabel Tosch<br>87512 Birkenried/Talheim</p>
  <div class="intro__phone">
    <p>0176 55501942</p>
    <span class="tag tag--rose">Termine nach Vereinbarung</span>
  </div>
  <div class="intro__rule"></div>
  <ul class="intro__social">
    <li>www.lumi-lash.de</li>
    <li><span class="dot"></span>@lumi_lash25</li>
    <li><span class="dot"></span>@lumi_lash_de</li>
  </ul>
</article>

<article class="flyer flyer--prices">
  <svg class="flyer__art" viewBox="0 0 360 730" aria-hidden="true">
    <defs>
      <linearGradient id="pricePhoto" x1="0" y1="0" x2="1" y2="0">
        <stop offset="0" stop-color="#e88fa8"/>
        <stop offset="0.6" stop-color="#f0b3c4"/>
        <stop offset="1" stop-color="#9a6a78"/>
      </linearGradient>
    </defs>
    <rect width="360" height="112" fill="url(#pricePhoto)" role="img" aria-label="Foto: Auge mit langen Wimpern und Lidschatten"/>
    <path d="M0,80 C100,90 200,122 360,96 L360,112 C260,135 120,120 0,100 Z" fill="var(--plum-dark)"/>
    <path d="M0,100 C120,120 260,135 360,112 L360,160 L0,160 Z" fill="var(--paper)"/>
  </svg>

  <h2 class="prices__title">LEISTUNGEN &amp; PREISE</h2>

  <div class="price-list">
    <section class="price-group">
      <h3 class="price-group__title">WIMPERNVERLÄNGERUNG</h3>
      <p class="price-group__sub">Natural Look Wimpern</p>
      <div class="price-row"><span class="price-row__label">Neuset</span><span class="price-row__cur">€</span><span class="price-row__amt">79,–</span></div>
      <div class="price-row"><span class="price-row__label">auffüllen 1–2 Wochen</span><span class="price-row__cur">€</span><span class="price-row__amt">35,–</span></div>
      <div class="price-row"><span class="price-row__label">auffüllen 3–4 Wochen</span><span class="price-row__cur">€</span><span class="price-row__amt">45,–</span></div>
      <p class="price-note">Auffüllen ab der 5.Woche = Neupreis</p>
      <p class="price-group__sub">Volumen Wimpern</p>
      <div class="price-row"><span class="price-row__label">Neuset</span><span class="price-row__cur">€</span><span class="price-row__amt">99,–</span></div>
      <div class="price-row"><span class="price-row__label">auffüllen 1–2 Wochen</span><span class="price-row__cur">€</span><span class="price-row__amt">35,–</span></div>
      <div class="price-row"><span class="price-row__label">auffüllen 3–4 Wochen</span><span class="price-row__cur">€</span><span class="price-row__amt">45,–</span></div>
      <p class="price-note">Auffüllen ab der 5.Woche = Neupreis</p>
    </section>

    <section class="price-group">
      <h3 class="price-group__title">LASH-LIFTING</h3>
      <div class="price-row"><span class="price-row__label">Lifting inkl. färben &amp; Keratin / Laminierung</span><span class="price-row__cur">€</span><span class="price-row__amt">XX,–</span></div>
    </section>

    <section class="price-group">
      <h3 class="price-group__title">WAXING</h3>
      <div class="price-row"><span class="price-row__label">Waxen/Zupfen (Augenbrauen, Damenbart)</span><span class="price-row__unit">je</span><span class="price-row__cur">€</span><span class="price-row__amt">5,–</span></div>
      <div class="price-row"><span class="price-row__label">Achseln</span><span class="price-row__cur">€</span><span class="price-row__amt">15,–</span></div>
    </section>

    <section class="price-group">
      <h3 class="price-group__title">MICROBLADING</h3>
      <div class="price-row gap-sm"><span class="price-row__label">feinste Härchenzeichnung (manuell)</span><span class="price-row__cur">€</span><span class="price-row__amt">269,–</span></div>
    </section>

    <section class="price-group">
      <h3 class="price-group__title">PERMANENT MAKE-UP</h3>
      <div class="price-row gap-sm"><span class="price-row__label">Powder Brows</span><span class="price-row__cur">€</span><span class="price-row__amt">300,–</span></div>
      <div class="price-row"><span class="price-row__label">Powder Brows Combo (Härchen&amp;Shading)</span><span class="price-row__cur">€</span><span class="price-row__amt">350,–</span></div>
      <div class="price-row"><span class="price-row__label">Wimpernkranzverdichtung (oben)</span><span class="price-row__cur">€</span><span class="price-row__amt">150,–</span></div>
      <div class="price-row"><span class="price-row__label">Lidstrich dekorativ</span><span class="price-row__cur">€</span><span class="price-row__amt">250,–</span></div>
      <div class="price-row"><span class="price-row__label">Velvet Lips</span><span class="price-row__cur">€</span><span class="price-row__amt">380,–</span></div>
      <div class="price-row"><span class="price-row__label">Lippen Vollschattierung</span><span class="price-row__cur">€</span><span class="price-row__amt">420,–</span></div>
      <div class="price-row"><span class="price-row__label">BB GLow</span><span class="price-row__cur">€</span><span class="price-row__amt">XX,–</span></div>
      <div class="price-row"><span class="price-row__label">Hyaluron Pen</span><span class="price-row__cur">€</span><span class="price-row__amt">XX,–</span></div>
    </section>
  </div>

  <div class="prices__footer">
    <span class="tag tag--plum">Termine nach Vereinbarung</span>
    <p class="prices__web">www.lumi-lash.de</p>
  </div>
  <p class="prices__brand brand-name">LUMI LASH</p>
</article>

</body>
</html>
```